Luxury skin care/beauty salon needs a fresh wordpress website makeover

Today we have a wordpress site that has served us well, and we want to stay with wordpress, but we need a new up to date fresh look, with an inviting and enticing front, and look that just draws people in to book an appoint for luxury beauty treatment.

The salon consists of beautisian/skin specialint, a cosmetical nurse, and a doctor, - so top notch expertice within skin care and beauty treatment.

- The site should be integrated with Postwren (which we currently do not use.

- The site should further be able to "show prices for treatments" in a manner that matches the new website in style and layout, - we do show prices today via ex. the booking module from a vendor, but its done via iFrame

- booking needs to be very easy and intuitive, and the site needs to be response, since 75% of our customers use Ipad or mobile phone while booking

- the colours of the logo and style for the company today is primarily gold and black, and the shop is kept in a minimalistic style

- we have fresh newly made professional pictures made, and we can also later supply a video for ex. a landing page

- we have a license for Bricklane if that can be utilized

- we need to be able to translate all elements into minimum Norwegian

- we use QV and Snapvista today to promote our services, if that can be incorporated, that would be a promotion plus

today we have the following pages
- main page
- a treatment page, where treatments are in more detail explained, this also doubles as pricelist ... we might look to discard this, since its manually updated and is not the master ... the master is the booking system, which also contains princes
- a portfolio page, seperated into types of treatments, this page also has one element of Snapvista which is one of the prime social media channals.
- a team member page, that presents the staff
- a contact us page
- a booking page ( that uses the national available booking system that we want to keep, but present in a different manner if possible) .. including gift card

we are not nessesarily looking to keep all pages, if the new design comes up with a more proffesional and smoother look, so this is debatable, so i have left the "How many web pages do you need designed?" to 4 pages .. again debatable

The final design should communicate luxury and professional skincare and beauty treatments, and easy booking.

Target Market(s)

Women or men that want to book a beauty or skin care treatment

Industry/Entity Type

Beauty and skin care salon

Coding

Coded - Design and coding required

Number of Pages Required

4 page

Colors

Designer to choose colors to be used in the design.

Requirements
Must have
• booking system, a connection to postwren, ability to change wording/language (Norwegian)
Nice to have
• video background, if it compliments the design
Should not have
• a new booking platform, we want to stick with the one we have

```html
<!DOCTYPE html>
<html lang="en">
<head>
<meta charset="utf-8">
<title>Aurelle – Luxury skin care &amp; beauty salon</title>
<link rel="stylesheet" href="https://fonts.googleapis.com/css2?family=Playfair+Display:wght@400;500&family=Mulish:ital,wght@0,400;0,600;0,700;0,800;1,400&family=Great+Vibes&display=swap">
<style>
:root{
  --gold:#e3b14c;
  --gold-light:#f3d98f;
  --gold-deep:#c8942f;
  --ink:#111111;
  --ink-soft:#1b1b1b;
  --text:#333333;
  --muted:#6f6f6f;
  --white:#ffffff;
  --line:#3a3a3a;
}
*{margin:0;padding:0;box-sizing:border-box}
html,body{width:1200px;height:4060px;overflow:hidden}
body{font-family:'Mulish',Arial,sans-serif;color:var(--text);background:var(--white);position:relative}
.abs{position:absolute}
.serif{font-family:'Playfair Display',Georgia,serif;font-weight:400}
.script{font-family:'Great Vibes',cursive}
.gold-btn{position:absolute;background:linear-gradient(90deg,var(--gold-deep),var(--gold-light));color:var(--ink);font-size:12px;font-weight:800;letter-spacing:.3px;display:flex;align-items:center;justify-content:center;text-transform:uppercase}
.gold-btn::before{content:"";position:absolute;left:14px;right:-1px;top:-6px;height:1px;background:var(--gold)}
.gold-btn::after{content:"";position:absolute;left:-1px;right:50px;bottom:-6px;height:1px;background:var(--gold)}
.ph{position:absolute}

/* top bar */
.topbar{position:absolute;left:0;top:0;width:1200px;height:32px;background:var(--gold);font-size:12px;font-weight:600;color:var(--ink)}
.topbar .item{position:absolute;top:0;height:32px;display:flex;align-items:center;gap:10px}
.social-tag{position:absolute;top:5px;height:22px;background:var(--ink);color:var(--white);font-size:10px;font-weight:700;display:flex;align-items:center;justify-content:center;padding:0 5px}

/* header + hero */
.hero{position:absolute;left:0;top:32px;width:1200px;height:626px;background:linear-gradient(100deg,#151515 0%,#1e1e1e 45%,#262626 100%);overflow:hidden}
.hero-photo{left:560px;top:75px;width:640px;height:551px;background:radial-gradient(ellipse at 55% 45%,#8a5a45 0%,#4a2e25 35%,#1e1a19 75%)}
.nav{position:absolute;left:0;top:0;width:1200px;height:75px;background:rgba(10,10,10,.85)}
.brand{position:absolute;left:160px;top:18px;font-family:'Playfair Display',serif;font-size:34px;color:var(--gold);letter-spacing:2px}
.nav-links{position:absolute;left:366px;top:30px;display:flex;gap:30px;font-size:12px;color:#cfcfcf;font-weight:600;text-transform:uppercase}
.nav-links .active{color:var(--white);position:relative}
.nav-links .active::after{content:"";position:absolute;left:14px;top:30px;border:6px solid transparent;border-bottom-color:var(--gold)}
.book-now{left:933px;top:21px;width:107px;height:34px;font-size:11px}
.slide-arrow{position:absolute;top:330px;width:44px;height:42px;background:#3a3a3a;display:flex;align-items:center;justify-content:center}
.hero-welcome{left:158px;top:188px;font-size:40px;color:var(--gold)}
.hero-title{left:158px;top:240px;font-size:62px;line-height:64px;color:var(--white)}
.hero-cta{left:159px;top:402px;width:158px;height:37px}
.hero-arc{position:absolute;left:-80px;top:560px;width:560px;height:200px;border-radius:50%;background:rgba(255,255,255,.04)}

/* why choose us */
.why{position:absolute;left:0;top:658px;width:1200px;height:612px;background:var(--white)}
.why h2{position:absolute;left:665px;top:150px;font-size:44px;line-height:48px;color:var(--ink)}
.why .lead{position:absolute;left:665px;top:260px;width:370px;font-size:13px;font-style:italic;color:var(--gold);line-height:20px}
.why p.body{position:absolute;left:665px;width:380px;font-size:13.5px;line-height:23px;color:#444}
.stats{position:absolute;left:665px;top:455px;width:375px;border-top:1px solid #e5e5e5;display:flex;justify-content:space-between;padding-top:24px}
.stat{text-align:center}
.stat b{display:block;font-size:31px;font-weight:400;color:var(--gold);line-height:34px}
.stat span{font-size:13px;color:#333}
.frame-line{position:absolute;border:2px solid var(--gold)}

/* treatments */
.treat{position:absolute;left:0;top:1270px;width:1200px;height:767px;background:var(--ink);color:var(--white)}
.treat h2{position:absolute;left:0;width:1200px;top:52px;text-align:center;font-size:44px}
.treat .sub{position:absolute;left:0;width:1200px;top:114px;text-align:center;font-size:13px;font-style:italic;color:#e8e8e8}
.tab{position:absolute;top:165px;width:280px;height:87px;border:1px solid #444;display:flex;align-items:center;gap:20px;padding-left:16px}
.tab.on{background:linear-gradient(90deg,var(--gold-deep),var(--gold-light));border-color:transparent;color:var(--ink)}
.tab.on::after{content:"";position:absolute;left:132px;bottom:-12px;border:8px solid transparent;border-top-color:var(--gold-light);border-bottom:0}
.tab .ico{width:44px;height:44px;border-radius:50%;border:2px solid var(--gold)}
.tab.on .ico{border-color:var(--ink)}
.tab h4{font-size:20px;font-weight:700;line-height:24px}
.tab small{font-size:13px;color:#cfcfcf}
.tab.on small{color:#3a2a10}
.round-arrow{position:absolute;width:34px;height:34px;border-radius:50%;background:#3a3a3a;display:flex;align-items:center;justify-content:center}
.treat-photo{left:188px;top:334px;width:346px;height:346px;border-radius:50%;background:radial-gradient(circle at 50% 55%,#e9cdb8 0%,#c9a58f 50%,#6b5548 100%)}
.price-title{position:absolute;left:607px;top:352px;font-size:28px}
.price-grid{position:absolute;left:607px;top:420px;width:416px;display:grid;grid-template-columns:1fr 1fr}
.price-cell{height:80px;display:flex;flex-direction:column;align-items:center;justify-content:center;font-size:13px;color:#e8e8e8}
.price-cell b{font-size:21px;color:var(--gold);font-weight:800;margin-top:4px}
.price-cell b sup{font-size:11px;font-weight:700}
.price-cell:nth-child(odd){border-right:1px solid var(--line)}
.price-cell:nth-child(-n+2){border-bottom:1px solid var(--line)}
.pricing-btn{left:607px;top:614px;width:156px;height:37px}

/* team */
.team{position:absolute;left:0;top:2037px;width:1200px;height:679px;background:var(--white)}
.team h2{position:absolute;left:0;width:1200px;top:48px;text-align:center;font-size:44px;color:var(--ink)}
.team .sub{position:absolute;left:380px;width:440px;top:114px;text-align:center;font-size:13px;font-style:italic;line-height:21px;color:#444}
.member{position:absolute;top:320px;width:271px;height:210px;background:#1a1a1a;clip-path:polygon(0 0,100% 0,100% 58%,50% 100%,0 58%);color:var(--white);text-align:center}
.member h3{font-family:'Playfair Display',serif;font-weight:400;font-size:24px;margin-top:78px}
.member p{font-size:14px;color:var(--gold);margin-top:2px}
.member-photo{position:absolute;top:190px;width:176px;height:176px;border-radius:50%;border:4px solid var(--white);background:radial-gradient(circle at 50% 40%,#d8bfae 0%,#8f7466 40%,#2a2421 80%)}
.member-accent{position:absolute;top:520px;width:80px;height:2px;background:var(--gold);transform:rotate(-30deg)}
.team-btn{left:531px;top:574px;width:139px;height:37px}

/* video */
.video{position:absolute;left:0;top:2716px;width:1200px;height:377px;background:var(--ink);overflow:hidden}
.video-photo{left:0;top:0;width:755px;height:377px;background:linear-gradient(120deg,#5c3e33 0%,#c9a18a 40%,#8c6b5c 70%,#3a2a24 100%)}
.video-panel{position:absolute;left:755px;top:0;width:445px;height:377px;background:#121212}
.video h2{position:absolute;left:826px;top:58px;font-size:44px;line-height:48px;color:var(--white)}
.play{position:absolute;left:707px;top:212px;width:96px;height:96px;border-radius:50%;background:rgba(255,255,255,.25);display:flex;align-items:center;justify-content:center}
.play span{width:70px;height:70px;border-radius:50%;background:var(--white);display:flex;align-items:center;justify-content:center}

/* reviews */
.reviews{position:absolute;left:0;top:3093px;width:1200px;height:370px;background:var(--white)}
.rv-brand{position:absolute;left:159px;top:58px;font-family:'Playfair Display',serif;font-size:32px;color:#4a7fdc}
.reviews h2{position:absolute;left:159px;top:100px;font-size:44px;line-height:48px;color:var(--ink)}
.reviews .according{position:absolute;left:159px;top:208px;font-size:13px;font-style:italic;color:#444}
.stars{color:var(--gold);letter-spacing:5px}
.review{position:absolute;top:68px;width:322px;height:230px;background:var(--white);box-shadow:0 4px 22px rgba(0,0,0,.09);padding:26px 17px}
.review .who{display:flex;gap:14px;align-items:center}
.review .av{width:66px;height:66px;border-radius:50%;background:radial-gradient(circle,#caa58f,#4d3a33)}
.review h5{font-size:15px;font-weight:600;color:#222}
.review time{font-size:11.5px;color:#555}
.review p{font-size:14px;line-height:22px;color:#444;margin-top:6px}
.dark-dot{position:absolute;width:36px;height:36px;border-radius:50%;background:#222;display:flex;align-items:center;justify-content:center}

/* subscribe */
.subscribe{position:absolute;left:0;top:3463px;width:1200px;height:265px;background:linear-gradient(90deg,#d8a63d 0%,#dfae45 50%,#c99632 100%);color:var(--white);text-align:center}
.subscribe h2{position:absolute;left:0;width:1200px;top:40px;font-size:44px}
.subscribe p{position:absolute;left:385px;width:430px;top:112px;font-size:13px;font-style:italic;line-height:20px}
.sub-form{position:absolute;left:389px;top:173px;display:flex;height:36px}
.sub-form .field{width:287px;background:var(--white);color:#555;font-size:13px;display:flex;align-items:center;padding-left:13px;text-align:left}
.sub-form .send{width:135px;background:var(--ink);font-size:12px;font-weight:800;display:flex;align-items:center;justify-content:center}

/* footer */
.footer{position:absolute;left:0;top:3728px;width:1200px;height:332px;background:#1c1c1c;color:#8d8d8d;font-size:13.5px}
.footer .brand{left:166px;top:54px}
.contact-row{position:absolute;left:159px;display:flex;align-items:center;gap:16px;line-height:20px}
.ring{width:38px;height:38px;border-radius:50%;border:2px solid var(--gold);display:flex;align-items:center;justify-content:center;flex:none}
.fcol{position:absolute;top:56px}
.fcol h4{font-family:'Playfair Display',serif;font-weight:400;font-size:20px;color:#e5e5e5;margin-bottom:12px}
.fcol li{list-style:none;line-height:24.4px}
.hours li{display:flex;justify-content:space-between;width:230px}
.copy{position:absolute;left:159px;top:290px;font-size:12px;color:#bdbdbd}
.fsocial{position:absolute;top:276px;height:34px;border-radius:17px;border:2px solid var(--gold);color:var(--white);font-size:10px;font-weight:700;display:flex;align-items:center;justify-content:center;padding:0 8px}
.footer-rule{position:absolute;left:159px;top:263px;width:881px;height:1px;background:#333}
</style>
</head>
<body>

<!-- top bar -->
<div class="topbar">
  <div class="item" style="left:160px">
    <svg width="20" height="20" viewBox="0 0 20 20"><rect x="1" y="1" width="18" height="18" rx="4" fill="none" stroke="#111" stroke-width="1.6"/><path d="M6 5.5c.5 4 3.5 8 8 9l1.2-2-2.3-1.3-1 1c-1.5-.7-2.8-2-3.5-3.5l1-1L8.1 5z" fill="#111"/></svg>
    Phone: (+47) 482 30 516
  </div>
  <div class="item" style="left:436px">
    <svg width="20" height="20" viewBox="0 0 20 20"><rect x="1" y="1" width="18" height="18" rx="4" fill="none" stroke="#111" stroke-width="1.6"/><path d="M5 7h10v7H5zM5 7l5 4 5-4" fill="none" stroke="#111" stroke-width="1.4"/></svg>
    Address: Storgata 42, 2609 Lillehammer
  </div>
  <div class="item" style="left:890px">ENG ▾</div>
  <div class="social-tag" style="left:980px">QV</div>
  <div class="social-tag" style="left:1008px">Snapvista</div>
</div>

<!-- header + hero -->
<header class="hero">
  <div class="ph hero-photo" role="img" aria-label="Portrait of a woman with bronze eye makeup and a black hat"></div>
  <div class="hero-arc"></div>
  <nav class="nav">
    <div class="brand">AURELLE</div>
    <div class="nav-links">
      <span class="active">Home</span><span>Treatment ▾</span><span>Portfolio</span><span>Team Member</span><span>Contact Us</span>
    </div>
    <div class="gold-btn book-now">Book Now</div>
  </nav>
  <div class="abs script hero-welcome">Welcome to aurelle</div>
  <h1 class="abs serif hero-title">Luxury skin care<br>&amp; beauty salon</h1>
  <div class="gold-btn hero-cta">Contact with us</div>
  <div class="slide-arrow" style="left:0"><svg width="12" height="16"><path d="M9 2L3 8l6 6" fill="none" stroke="#ddd" stroke-width="1.6"/></svg></div>
  <div class="slide-arrow" style="right:0"><svg width="12" height="16"><path d="M3 2l6 6-6 6" fill="none" stroke="#ddd" stroke-width="1.6"/></svg></div>
</header>

<!-- why choose us -->
<section class="why">
  <div class="frame-line" style="left:414px;top:115px;width:92px;height:70px;border-left:0;border-bottom:0"></div>
  <div class="frame-line" style="left:505px;top:176px;width:75px;height:0;border-width:2px 0 0 0"></div>
  <div class="frame-line" style="left:208px;top:358px;width:96px;height:200px;border-right:0;border-top:0"></div>
  <div class="frame-line" style="left:303px;top:470px;width:0;height:130px;border-width:0 0 0 2px"></div>
  <div class="ph" role="img" aria-label="Beauty products and salon details" style="left:415px;top:125px;width:175px;height:420px;background:linear-gradient(160deg,#e9d6c8,#b98d6f 55%,#6d3f2e)"></div>
  <div class="ph" role="img" aria-label="Skin care device and dried flowers" style="left:219px;top:330px;width:276px;height:195px;background:linear-gradient(135deg,#c9ab86,#e6ddd2 55%,#a88b6a)"></div>
  <div class="ph" role="img" aria-label="Flowers on a pale backdrop" style="left:313px;top:470px;width:277px;height:122px;background:linear-gradient(90deg,#ece7e2,#f7f5f2)"></div>
  <div class="ph" role="img" aria-label="Client receiving a facial treatment" style="left:159px;top:78px;width:256px;height:256px;background:linear-gradient(135deg,#9fd0cc 0%,#e4c2ad 50%,#c9977c 100%)"></div>

  <h2 class="serif">Why our clients<br>choose us</h2>
  <p class="lead">The salon consists of beautisian/skin specialist, a cosmetical nurse, and a doctor.</p>
  <p class="body" style="top:312px">Beauty salon in central Lillehammer. We focus on high competence, exceptional service and the feeling of luxury in everyday life.</p>
  <p class="body" style="top:390px">The salon was established in the beginning of 2021 by Selma and Mari Elise.</p>
  <div class="stats">
    <div class="stat"><b>85+</b><span>Happy Customer</span></div>
    <div class="stat"><b>15+</b><span>Team Member</span></div>
    <div class="stat"><b>25+</b><span>Worldwide Salon</span></div>
  </div>
</section>

<!-- treatments -->
<section class="treat">
  <h2 class="serif">Our treatments</h2>
  <div class="sub">10% student and military discount on all treatments</div>
  <div class="round-arrow" style="left:128px;top:192px"><svg width="10" height="14"><path d="M7 2L2 7l5 5" fill="none" stroke="#ddd" stroke-width="1.5"/></svg></div>
  <div class="tab" style="left:172px"><div class="ico"></div><div><h4>Facial Makeup</h4><small>Treatment</small></div></div>
  <div class="tab on" style="left:459px"><div class="ico"></div><div><h4>Medical Skin Care</h4><small>Treatment</small></div></div>
  <div class="tab" style="left:747px"><div class="ico"></div><div><h4>All Hair Removal</h4><small>Treatment</small></div></div>
  <div class="round-arrow" style="left:1038px;top:192px"><svg width="10" height="14"><path d="M3 2l5 5-5 5" fill="none" stroke="#ddd" stroke-width="1.5"/></svg></div>

  <svg class="abs" style="left:161px;top:307px" width="400" height="400" viewBox="0 0 400 400">
    <circle cx="200" cy="200" r="188" fill="none" stroke="#f0d48a" stroke-width="6" stroke-dasharray="150 30 60 24 220 40 90 26" stroke-linecap="round"/>
    <circle cx="200" cy="200" r="174" fill="none" stroke="#f0d48a" stroke-width="4" stroke-dasharray="40 300 120 400" stroke-linecap="round"/>
  </svg>
  <div class="ph treat-photo" role="img" aria-label="Client receiving a gloved forehead skin treatment"></div>

  <h3 class="serif price-title">Service list &amp; pricing</h3>
  <div class="price-grid">
    <div class="price-cell">Scar resolution incl<b>2790<sup>/kr</sup></b></div>
    <div class="price-cell">Scar resolution<b>1150<sup>/kr</sup></b></div>
    <div class="price-cell">Dermapen<b>2200<sup>/kr</sup></b></div>
    <div class="price-cell">TCA touch<b>1450<sup>/kr</sup></b></div>
  </div>
  <div class="gold-btn pricing-btn">View all pricing</div>
</section>

<!-- team -->
<section class="team">
  <h2 class="serif">Our professional team</h2>
  <p class="sub">We put perfection and expertise at the top of the list, so that it is safe and good to get treatment from us at Aurelle.</p>

  <div class="member" style="left:159px"><h3>Selma R. Haugen</h3><p>Owner General Manager</p></div>
  <div class="member" style="left:465px"><h3>Mari Elise Lundberg</h3><p>Owner Deputy Manager</p></div>
  <div class="member" style="left:771px"><h3>Dr. Hedda Strand</h3><p>Law</p></div>
  <div class="ph member-photo" style="left:206px" role="img" aria-label="Portrait of the general manager"></div>
  <div class="ph member-photo" style="left:512px" role="img" aria-label="Portrait of the deputy manager in a white coat"></div>
  <div class="ph member-photo" style="left:818px" role="img" aria-label="Portrait of the doctor in a white coat"></div>
  <div class="member-accent" style="left:280px"></div>
  <div class="member-accent" style="left:586px"></div>
  <div class="member-accent" style="left:892px"></div>

  <div class="gold-btn team-btn">View all team</div>
</section>

<!-- video -->
<section class="video">
  <div class="ph video-photo" role="img" aria-label="Practitioner treating a client's face at the salon"></div>
  <div class="video-panel"></div>
  <h2 class="serif">How we <u style="text-decoration-color:#fff;text-underline-offset:6px;text-decoration-thickness:1px">do</u><br>this</h2>
  <svg class="abs" style="left:848px;top:178px" width="40" height="48" viewBox="0 0 40 48"><path d="M6 4c20 4 26 22 14 36" fill="none" stroke="#fff" stroke-width="1.6"/><path d="M13 34l7 7 6-9" fill="none" stroke="#fff" stroke-width="1.6"/></svg>
  <div class="abs script" style="left:826px;top:236px;font-size:26px;color:var(--gold)">Click the play button</div>
  <div class="abs" style="left:826px;top:270px;font-size:20px;color:#fff">To watch a video</div>
  <div class="play"><span><svg width="26" height="28"><path d="M3 2l22 12L3 26z" fill="#e3b14c"/></svg></span></div>
  <div class="abs" style="left:755px;top:372px;width:320px;height:5px;background:var(--gold)"></div>
</section>

<!-- reviews -->
<section class="reviews">
  <div class="rv-brand">Reviewly</div>
  <h2 class="serif">Customer<br>reviews</h2>
  <div class="according">According to 5 reviews.</div>
  <div class="abs stars" style="left:159px;top:228px;font-size:21px">★★★★★</div>
  <div class="dark-dot" style="left:159px;top:283px"><svg width="10" height="14"><path d="M7 2L2 7l5 5" fill="none" stroke="#fff" stroke-width="1.5"/></svg></div>
  <div class="dark-dot" style="left:205px;top:283px"><svg width="10" height="14"><path d="M3 2l5 5-5 5" fill="none" stroke="#fff" stroke-width="1.5"/></svg></div>

  <article class="review" style="left:384px">
    <div class="who"><div class="av" role="img" aria-label="Reviewer photo"></div><div><h5>Randi K</h5><time>4. Mai, 2021.</time></div></div>
    <div class="stars" style="font-size:15px;margin-top:8px">★★★★★</div>
    <p>Got put on absolutely wonderful and beautiful lashes. You have to visit this place whether you are young or old like me, for nice blire.</p>
  </article>
  <article class="review" style="left:717px">
    <div class="who"><div class="av" role="img" aria-label="Reviewer photo"></div><div><h5>Sofie Berg</h5><time>19. Mai, 2021.</time></div></div>
    <div class="stars" style="font-size:15px;margin-top:8px">★★★★★</div>
    <p>What a service and professionalism on these young women !! Best place in lillehammer in my eyes :)</p>
  </article>
</section>

<!-- subscribe -->
<section class="subscribe">
  <h2 class="serif">Subscribe <u style="text-underline-offset:7px;text-decoration-thickness:1px">us</u></h2>
  <p>Lorem ipsum dolor sit amet consectetur adipisicing elit, sed do eiusmod tempor incididunt ut labore et dolore magna</p>
  <div class="sub-form"><div class="field">Enter your email.</div><div class="send">SUBSCRIBE US</div></div>
</section>

<!-- footer -->
<footer class="footer">
  <div class="brand">AURELLE</div>
  <div class="contact-row" style="top:127px">
    <span class="ring"><svg width="14" height="18" viewBox="0 0 14 18"><path d="M7 1a6 6 0 0 1 6 6c0 4-6 10-6 10S1 11 1 7a6 6 0 0 1 6-6z" fill="#fff"/><circle cx="7" cy="7" r="2.2" fill="#1c1c1c"/></svg></span>
    <span>Storgata 42,<br>2609 Lillehammer</span>
  </div>
  <div class="contact-row" style="top:190px">
    <span class="ring"><svg width="16" height="16" viewBox="0 0 16 16"><path d="M3 1.5c.5 6 4.5 11 11 12l1-3-3.5-1.5-1.5 1.5C8 9.5 6.5 8 5.5 6l1.5-1.5L5.5 1z" fill="#fff"/></svg></span>
    <span>(+47) 482 30 516</span>
  </div>

  <div class="fcol" style="left:454px"><h4>Sitemap</h4><ul><li>Home</li><li>Treatment</li><li>Portfolio</li><li>Team Member</li><li>Contact Us</li></ul></div>
  <div class="fcol" style="left:616px"><h4>About Aurelle AS</h4><ul><li>Privacy Policy</li><li>Cookies</li><li>Terms &amp; Condition</li><li>GDPR</li><li>Covid Information</li></ul></div>
  <div class="fcol hours" style="left:810px"><h4>Opening Hour</h4><ul>
    <li><span>Monday</span><span>09.00 - 16.00</span></li>
    <li><span>Tuesday</span><span>09.00 - 19.00</span></li>
    <li><span>Wednesday</span><span>09.00 - 16.00</span></li>
    <li><span>Thrusday</span><span>09.00 - 19.00</span></li>
    <li><span>Friday</span><span>09.00 - 16.00</span></li>
    <li><span>Saturday</span><span>By Appoinment</span></li>
  </ul></div>

  <div class="footer-rule"></div>
  <div class="copy">© 2021 Aurelle.All Rights Reserved</div>
  <div class="fsocial" style="left:966px">QV</div>
  <div class="fsocial" style="left:1006px;width:auto">Snapvista</div>
</footer>

</body>
</html>
```